Letterhead for 3 attorney Workers' Comp law firm

We are a 3 attorney law office. We specialize in Workers' Compensation. Our office represents workers who are injured on the job, and the estates of workers who are killed one the job.
When we started our office, we created our own letterhead & have been using it for years. We've just recently hired the 3rd attorney, and were going to just add his name to the letterhead, but have decided we wanted to get a professionally designed letterhead and business cards at this point.
We want something that looks clean and professional. It must look good in black and white because we often make multiple copies of our documents. We're hoping for a design that resonates confidence, reliability and experience.
The design must include the firm name: Dorrance & Pike, PLLC. We would like the PLLC to be small compared to the Dorrance & Pike graphic. We also want to incorporate the attorney names: Ulric Dorrance, Janet Pike, and Lyle Hagberg. Our current letterhead has our contact info in the footer at the bottom of the page. We like that design, but are open to the idea of having it at the top. We'll leave that at the discretion of the designer. Our contact info is as follows: 472 S. Larchmont Avenue, Suite 315 Bellingham, WA 98117 Phone: 360-514-2967, Fax: 360-521-6079, and our website: www.dorrancepike-law.example
Target Market(s)
Clients, courts, other legal offices, doctors offices. These are the people who see our letterhead most frequently. It's not so much for marketing purposes, mainly so that we have a professional image when sending out documents.
Industry/Entity Type
Law Firm
Contact Information for Business Card
On the back of the business card: it can be designed, or be a template for filling in appointment reminder information (i.e. date, time, etc)
Colors
Designer to choose colors to be used in the design.
Requirements
Must have
- Must have our firm name at the top.
- Must include the attorney names.
- Must have all of our contact information (can be at top or bottom - whatever looks best with the design)
Nice to have
- A strong, confident design
Should not have
- We don't want the design to be playful, cartoony or busy.

```html
<!DOCTYPE html>
<html lang="en">
<head>
<meta charset="utf-8">
<title>Dorrance &amp; Pike, PLLC — Letterhead</title>
<link rel="stylesheet" href="https://fonts.googleapis.com/css2?family=Arimo:wght@400;700&display=swap">
<style>
  :root {
    --backdrop: #4a4a4a;
    --paper: #ffffff;
    --brown-dark: #6e3b1e;
    --brown-mid: #7a4424;
    --tan: #bf8a6c;
    --ink: #111111;
    --gray-text: #555555;
  }
  * { margin: 0; padding: 0; box-sizing: border-box; }
  html, body {
    width: 900px; height: 1200px; overflow: hidden;
    background: var(--backdrop);
    font-family: "Arimo", Arial, sans-serif;
  }
  .letterhead {
    position: absolute; left: 79px; top: 141px;
    width: 744px; height: 968px;
    background: var(--paper);
  }
  .rules { position: absolute; inset: 0; width: 744px; height: 968px; }
  .rules path { fill: none; stroke: var(--brown-dark); stroke-width: 2.5; }
  .firm-mark {
    position: absolute; left: 48px; top: 48px;
    display: flex; align-items: flex-start; gap: 10px;
  }
  .firm-mark__square { width: 22px; height: 22px; background: var(--brown-dark); margin-top: 4px; }
  .firm-name {
    color: var(--brown-dark); font-weight: 700;
    font-size: 21px; line-height: 1.15; letter-spacing: 0.5px;
    text-transform: uppercase;
  }
  .firm-name__suffix { font-size: 12px; letter-spacing: 1.5px; }
  .attorneys {
    position: absolute; left: 20px; top: 190px; width: 160px;
    text-align: center;
  }
  .attorneys__label { font-size: 10px; color: #333; margin-bottom: 4px; }
  .attorneys__name { font-size: 14px; font-weight: 700; line-height: 19px; color: var(--brown-mid); }
  .attorneys__name--associate { color: var(--tan); }
  .body-copy {
    position: absolute; left: 178px; top: 266px;
    font-size: 11.4px; line-height: 22px; color: var(--ink);
    white-space: nowrap;
  }
  .contact {
    position: absolute; left: 0; width: 802px; top: 862px;
    text-align: center; color: var(--gray-text);
    font-size: 16px; line-height: 21.5px;
  }
</style>
</head>
<body>
  <main class="letterhead">
    <svg class="rules" viewBox="0 0 744 968" aria-hidden="true">
      <path d="M48 182 H580 L744 0"/>
      <path d="M0 968 L122 843 H744"/>
    </svg>

    <header class="firm-mark">
      <div class="firm-mark__square"></div>
      <div class="firm-name">Dorrance &amp;<br>Pike <span class="firm-name__suffix">PLLC</span></div>
    </header>

    <section class="attorneys">
      <p class="attorneys__label">Attorneys :</p>
      <p class="attorneys__name">Ulric Dorrance</p>
      <p class="attorneys__name">Janet Pike</p>
      <p class="attorneys__name attorneys__name--associate">Lyle Hagberg</p>
    </section>

    <article class="body-copy">
      Sample Text Sample TextSample TextSample TextSample TextSample TextSample T<br>
      TextSample TextSample TextSample TextSample TextSample TextSample TextSample<br>
      TextSample TextSample TextSample TextSample TextSample TextSample TextSample<br>
      TextSample TextSample TextSample TextSample TextSample TextSample TextSample<br>
      TextSample TextSample TextSample TextSample TextSample TextSample TextSample<br>
      TextSample TextSample TextSample TextSample TextSample TextSample TextSample<br>
      TextSample TextSample TextSample TextSample TextSample TextSample TextSample<br>
      TextSample TextSample TextSample TextSample TextSample TextSample TextSample<br>
      TextSample TextSample TextSample TextSample TextSample TextSample TextSample<br>
      TextSample TextSample TextSample TextSample TextSample TextSample TextSample<br>
      TextSample TextSample TextSample TextSample TextSample TextSample TextSample<br>
      TextSample TextSample TextSample TextSample TextSample TextSample TextSample<br>
      TextSample TextSample TextSample TextSample TextSample TextSample TextSample<br>
      TextSample TextSample TextSample TextSample TextSample TextSample TextSample<br>
      TextSample TextSample TextSample TextSample TextSample TextSample TextSample<br>
      TextSample TextSample TextSample TextSample TextSample TextSample TextSample<br>
      TextSample TextSample TextSample TextSample TextSample TextSample TextSample<br>
      TextSample TextSample TextSample TextSample TextSample TextSample TextSample<br>
      TextSample TextSample TextSample TextSample TextSample TextSample TextSample<br>
      TextSample TextSample TextSample TextSample TextSample TextSample TextSample<br>
      TextSample TextSample TextSample TextSample TextSample TextSample TextSample<br>
      TextSample TextSample TextSample TextSample TextSample TextSample TextSample
    </article>

    <footer class="contact">
      <p>472 S. Larchmont Avenue, Suite 315 Bellingham, WA 98117</p>
      <p>Phone: 360-514-2967, Fax: 360-521-6079</p>
      <p>website: www.dorrancepike-law.example</p>
    </footer>
  </main>
</body>
</html>
```